Brisbo Excavation and Landscaping

I need a double sided card thick with rounded edges. I want an identical card of one of your designs but with my name on it on one side. Othe side I want my name,number under owner operator and a list of what I do. , drainage,grading,trenching stump removal , postholes. Landscaping lawn renovations, and reconfigurations, small to large rip outs and installs,sod work and burms and swails for water run off and plantings the two pictures of cards is what I like
Updates

Project Deadline Extended
Reason: First time doing this not sure if two days was enough, no one was taking on project so trying to figure out why I posted a picture of what I want so should be relatively easy

Industry/Entity Type

Landscaping

Contact Information for Business Card

Name Ted Brisbo
Palm beach county Phone 860-555-0142

Font styles to use
Other font styles liked:
• It's on card I sent second one

Requirements
Must have
• Same colors and look of card at bottom
Nice to have
• All aspects of excavation and landscaping on back of card
• Will add web address at end

```html
<!DOCTYPE html>
<html lang="en">
<head>
<meta charset="utf-8">
<title>Brisbo Excavation – Business Card</title>
<link href="https://fonts.googleapis.com/css2?family=Arimo:wght@400;700&family=Roboto+Condensed:wght@400;700&display=swap" rel="stylesheet">
<style>
  :root {
    --page-bg: #e3e5e7;
    --card-white: #ffffff;
    --brand-orange: #e59a00;
    --ground-dark: #242424;
    --title-slate: #566a73;
    --contact-text: #4a545b;
    --icon-slate: #5f6f76;
    --sky-grey: #dfe6e4;
    --machine-yellow: #f2ab0f;
    --owner-light: #f2f2f2;
  }
  * { margin: 0; padding: 0; box-sizing: border-box; }
  html, body {
    width: 959px; height: 1200px; overflow: hidden;
    background: var(--page-bg);
    font-family: "Arimo", Arial, sans-serif;
  }
  .canvas { position: relative; width: 959px; height: 1200px; }

  .card {
    position: absolute;
    width: 763px; height: 457px;
    background: var(--card-white);
    border-radius: 17px;
    overflow: hidden;
  }
  .card--front { left: 105px; top: 77px; }
  .card--back { left: 98px; top: 600px; }

  .front__top-band {
    position: absolute; left: 0; top: 0; width: 100%; height: 64px;
    background: var(--brand-orange);
  }
  .front__bottom-band {
    position: absolute; left: 0; bottom: 0; width: 100%; height: 66px;
    background: var(--ground-dark);
  }
  .front__machine {
    position: absolute; left: 110px; top: 111px; width: 230px; height: 126px;
    background: linear-gradient(180deg, var(--machine-yellow) 0%, #d8950a 70%, var(--ground-dark) 100%);
    border-radius: 10px;
  }
  .front__title {
    position: absolute; left: 372px; top: 110px;
    font-weight: 700; font-size: 54px; line-height: 56px;
    color: var(--title-slate);
  }

  .contact-row {
    position: absolute; left: 0; top: 296px; width: 100%; height: 40px;
  }
  .contact-item {
    position: absolute; top: 0; height: 40px;
    display: flex; align-items: center;
    font-size: 18px; color: var(--contact-text);
    white-space: nowrap;
  }
  .contact-item svg { fill: var(--icon-slate); flex: none; }
  .contact-item--name { left: 50px; gap: 22px; }
  .contact-item--phone { left: 294px; gap: 10px; }
  .contact-item--place { left: 494px; gap: 14px; }

  .back__services {
    position: absolute; left: 22px; top: 50px; width: 705px;
    font-family: "Roboto Condensed", "Arial Narrow", sans-serif;
    font-weight: 700; font-size: 17px; line-height: 24px;
    color: var(--brand-orange);
  }
  .back__scene {
    position: absolute; left: 0; top: 144px; width: 100%; height: 184px;
    background: linear-gradient(180deg, #ffffff 0%, var(--sky-grey) 45%, #cfd8d6 100%);
  }
  .back__ground {
    position: absolute; left: 0; bottom: 0; width: 100%; height: 129px;
    background: var(--ground-dark);
  }
  .back__owner {
    position: absolute; left: 22px; bottom: 22px;
    font-family: "Roboto Condensed", "Arial Narrow", sans-serif;
    color: var(--owner-light);
  }
  .back__owner-label {
    font-weight: 700; font-size: 15px; line-height: 20px;
    letter-spacing: 1px; text-transform: uppercase;
    color: var(--brand-orange);
  }
  .back__owner-details {
    font-weight: 400; font-size: 17px; line-height: 24px;
  }
</style>
</head>
<body>
<main class="canvas">

  <section class="card card--front" aria-label="Card front">
    <div class="front__top-band"></div>
    <div class="front__machine" role="img" aria-label="Illustration of a yellow tracked excavator"></div>
    <h1 class="front__title">Brisbo<br>Excavation</h1>

    <div class="contact-row">
      <div class="contact-item contact-item--name">
        <svg width="30" height="30" viewBox="0 0 30 30" aria-hidden="true">
          <circle cx="15" cy="9" r="7"/>
          <path d="M1 30 C1 20 7 17 15 17 C23 17 29 20 29 30 Z"/>
        </svg>
        <span>Ted Brisbo</span>
      </div>
      <div class="contact-item contact-item--phone">
        <svg width="26" height="26" viewBox="0 0 24 24" aria-hidden="true">
          <path d="M6.6 10.8c1.4 2.8 3.8 5.1 6.6 6.6l2.2-2.2c.3-.3.7-.4 1-.2 1.1.4 2.3.6 3.6.6.6 0 1 .4 1 1V20c0 .6-.4 1-1 1C10.6 21 3 13.4 3 4c0-.6.4-1 1-1h3.5c.6 0 1 .4 1 1 0 1.3.2 2.5.6 3.6.1.3 0 .7-.2 1z"/>
        </svg>
        <span>860-555-0142</span>
      </div>
      <div class="contact-item contact-item--place">
        <svg width="22" height="30" viewBox="0 0 22 30" aria-hidden="true">
          <path d="M11 0C4.9 0 0 4.9 0 11c0 8 11 19 11 19s11-11 11-19C22 4.9 17.1 0 11 0zm0 15.5a4.5 4.5 0 1 1 0-9 4.5 4.5 0 0 1 0 9z"/>
        </svg>
        <span>Palm Beach County</span>
      </div>
    </div>

    <div class="front__bottom-band"></div>
  </section>

  <section class="card card--back" aria-label="Card back">
    <p class="back__services">Drainage,grading,trenching stump removal , postholes. Landscaping lawn renovations, and reconfigurations, small to large rip outs and installs,sod work and burms and swails for water run off and plantings</p>
    <div class="back__scene" role="img" aria-label="Illustration of a construction site with factory buildings, an excavator digging and a dump truck"></div>
    <div class="back__ground"></div>
    <div class="back__owner">
      <p class="back__owner-label">Owner Operator</p>
      <p class="back__owner-details">Ted Brisbo &nbsp;·&nbsp; 860-555-0142</p>
    </div>
  </section>

</main>
</body>
</html>
```